removed valdremo remodel

Redesign removed page to match website style with more dynamic capabilities, messaging, commerce, etc.

My website address is:
Www.valdremo.consulting for corporate styling, and flavour of approach and service offered.

Target Market(s)

Small, Medium Enterprise looking for business coaching and single entrepreneurs startups looking for advice and coaching.

Font styles to use
Sans Serif

Colors
276eb1

Requirements
Must have
• Match removed page style to website for branding.
• Contact information
• Services offered
• Links to website, email, Twitter, blogging. Messaging.
• (Will upload images and other data soonest).
Nice to have
• E-commerce,

```html
<!DOCTYPE html>
<html lang="en">
<head>
<meta charset="utf-8">
<title>VD Consulting – Page</title>
<link rel="stylesheet" href="https://fonts.googleapis.com/css2?family=Roboto:wght@400;500;700&family=Montserrat:wght@300;600&family=Abel&display=swap">
<style>
  :root{
    --brand:#1c5594;
    --brand-light:#276eb1;
    --bar:#4267b2;
    --page-bg:#e9ebee;
    --card:#ffffff;
    --line:#dddfe2;
    --text:#1d2129;
    --muted:#606770;
    --link:#385898;
    --green:#42b72a;
  }
  html,body{margin:0;padding:0;overflow:hidden;}
  body{background:var(--page-bg);font-family:"Roboto",Arial,sans-serif;color:var(--text);}
  .canvas{position:relative;width:1200px;height:850px;overflow:hidden;background:var(--page-bg);}
  .abs{position:absolute;white-space:nowrap;}

  .top-bar{position:absolute;left:0;top:0;width:1200px;height:37px;background:var(--bar);}
  .search{position:absolute;left:110px;top:8px;width:384px;height:21px;background:#fff;border-radius:2px;font-size:12px;line-height:21px;padding-left:8px;box-sizing:border-box;}
  .search svg{position:absolute;right:10px;top:4px;}

  .profile-pic{position:absolute;left:85px;top:49px;width:154px;height:154px;border-radius:50%;background:#fff;border:2px solid #f0f1f3;box-sizing:border-box;display:flex;align-items:center;justify-content:center;}
  .profile-pic span{font-family:"Abel",sans-serif;color:var(--brand);font-size:20px;}
  .page-name{left:86px;top:215px;font-size:18px;line-height:22px;}
  .page-handle{left:86px;top:238px;font-size:13px;line-height:16px;color:var(--muted);font-weight:500;}
  .nav-item{left:88px;font-size:12.5px;line-height:20px;}
  .nav-active{position:absolute;left:81px;top:348px;width:158px;height:24px;background:#f5f6f7;border-radius:2px;}
  .create-btn{position:absolute;left:86px;top:441px;width:83px;height:20px;background:var(--green);color:#fff;font-size:11px;font-weight:700;text-align:center;line-height:20px;border-radius:2px;}

  .cover{position:absolute;left:250px;top:37px;width:702px;height:269px;}
  .action-bar{position:absolute;left:250px;top:306px;width:702px;height:43px;background:#fff;}
  .btn{position:absolute;top:10px;height:23px;border:1px solid #ccd0d5;background:#f5f6f7;font-size:11px;font-weight:700;color:#4b4f56;line-height:23px;text-align:center;box-sizing:border-box;}
  .btn-email{background:var(--bar);color:#fff;border-color:var(--bar);font-weight:400;font-size:12px;border-radius:2px;}
  .btn-message{font-weight:400;font-size:12px;border-radius:2px;}

  .about-card{position:absolute;left:250px;top:362px;width:702px;height:500px;background:var(--card);border:1px solid var(--line);border-radius:3px;box-sizing:border-box;}
  .card-title{left:267px;top:376px;font-size:14px;font-weight:700;line-height:17px;}
  .suggest-link{left:856px;top:377px;font-size:10.5px;font-weight:700;color:var(--link);line-height:14px;}
  .section-head{font-size:11.5px;font-weight:700;color:var(--muted);letter-spacing:.3px;line-height:14px;}
  .rule{position:absolute;height:1px;background:var(--line);}
  .info-row{left:294px;font-size:12px;line-height:15px;}
  .info-link{color:var(--link);}
  .info-note{left:294px;font-size:10px;line-height:13.5px;white-space:normal;width:262px;}
  .icon{position:absolute;left:274px;}
  .avatar{position:absolute;left:613px;top:456px;width:27px;height:27px;border-radius:50%;background:radial-gradient(circle at 45% 40%,#d8a88a,#7a5544);}
  .member-name{left:647px;top:462px;font-size:12.5px;font-weight:700;color:var(--link);line-height:15px;}
</style>
</head>
<body>
<div class="canvas">

  <header class="top-bar">
    <div class="search">VD Consulting
      <svg width="13" height="13" viewBox="0 0 13 13"><circle cx="5.5" cy="5.5" r="4.3" fill="none" stroke="#4b4f56" stroke-width="1.5"/><line x1="8.7" y1="8.7" x2="12.3" y2="12.3" stroke="#4b4f56" stroke-width="1.6"/></svg>
    </div>
  </header>

  <aside>
    <div class="profile-pic"><span>VD Consulting</span></div>
    <div class="abs page-name">VD Consulting</div>
    <div class="abs page-handle">@Valdremoconsulting</div>
    <div class="nav-active"></div>
    <div class="abs nav-item" style="top:268px">Home</div>
    <div class="abs nav-item" style="top:295px">Photos</div>
    <div class="abs nav-item" style="top:323px">Posts</div>
    <div class="abs nav-item" style="top:350px;font-weight:700">About</div>
    <div class="abs nav-item" style="top:378px">Community</div>
    <div class="abs nav-item" style="top:405px">Info and ads</div>
    <div class="create-btn">Create a Page</div>
  </aside>

  <svg class="cover" viewBox="0 0 702 269" xmlns="http://www.w3.org/2000/svg">
    <defs>
      <linearGradient id="photoTone" x1="0" y1="0" x2="1" y2="1">
        <stop offset="0" stop-color="#d9d6d2"/>
        <stop offset="0.45" stop-color="#eceae7"/>
        <stop offset="1" stop-color="#c9c7c4"/>
      </linearGradient>
    </defs>
    <rect class="cover-photo" width="702" height="269" fill="url(#photoTone)" role="img" aria-label="Photo of a smiling businessman with glasses working on a laptop in a bright office"/>
    <polygon points="572,0 702,0 702,269 380,269" fill="#ffffff"/>
    <polygon points="558,0 572,0 380,269 366,269" fill="var(--brand)"/>
    <polygon points="385,246 702,246 702,269 368,269" fill="var(--brand)"/>
    <polygon points="0,136 462,136 410,210 0,210" fill="var(--brand)"/>
    <text x="11" y="164" font-family="Montserrat,sans-serif" font-weight="300" font-size="24" fill="#fff" textLength="339" lengthAdjust="spacingAndGlyphs">Are you looking for support in</text>
    <text x="11" y="196" font-family="Montserrat,sans-serif" font-weight="600" font-size="25" fill="#fff" textLength="394" lengthAdjust="spacingAndGlyphs">startups for advice and coaching</text>

    <text x="631" y="58" text-anchor="middle" font-family="Abel,sans-serif" font-size="21" fill="var(--brand)">VD Consulting</text>

    <g stroke="var(--brand)" stroke-width="3" fill="var(--brand)">
      <line x1="484" y1="117" x2="502" y2="117"/><circle cx="502" cy="117" r="3.5"/>
      <line x1="466" y1="143" x2="515" y2="143"/><circle cx="515" cy="143" r="3.5"/>
      <line x1="446" y1="169" x2="472" y2="169"/><circle cx="472" cy="169" r="3.5"/>
      <line x1="426" y1="195" x2="470" y2="195"/><circle cx="470" cy="195" r="3.5"/>
    </g>
    <g font-family="Abel,sans-serif" fill="var(--brand)" text-anchor="end">
      <text x="690" y="122" font-size="16" textLength="180" lengthAdjust="spacingAndGlyphs">Personal Business Coaching</text>
      <text x="687" y="148" font-size="16" textLength="162" lengthAdjust="spacingAndGlyphs">SME Business Consulting</text>
      <text x="690" y="174" font-size="16" textLength="208" lengthAdjust="spacingAndGlyphs">E-commerce Consulting services</text>
      <text x="690" y="200" font-size="16" textLength="206" lengthAdjust="spacingAndGlyphs">Ecommerce Marketing Coaching</text>
      <text x="690" y="226" font-size="15" textLength="264" lengthAdjust="spacingAndGlyphs">27, Ashbourne Road, Hartwell, TS417QX</text>
      <text x="690" y="242" font-size="10.5" textLength="264" lengthAdjust="spacingAndGlyphs">Tel : +44-7700-900314  ▌ martin.hale@valdremo.consulting</text>
    </g>
    <text x="444" y="264" font-family="Abel,sans-serif" font-size="17" fill="#fff">Connect With Us :</text>
    <g fill="none" stroke="#fff" stroke-width="2">
      <circle cx="578" cy="258" r="7.5"/><circle cx="602" cy="258" r="7.5"/><circle cx="626" cy="258" r="7.5"/>
    </g>
  </svg>

  <div class="action-bar">
    <div class="btn" style="left:11px;width:52px">Like</div>
    <div class="btn" style="left:62px;width:66px">Follow</div>
    <div class="btn" style="left:127px;width:65px">Share</div>
    <div class="btn" style="left:191px;width:30px">···</div>
    <div class="btn btn-email" style="left:446px;width:119px">Send Email</div>
    <div class="btn btn-message" style="left:576px;width:117px">Send Message</div>
  </div>

  <section class="about-card"></section>
  <div class="abs card-title">About</div>
  <div class="abs suggest-link">✎ Suggest Edits</div>

  <div class="abs section-head" style="left:274px;top:418px">BUSINESS INFO</div>
  <div class="rule" style="left:274px;top:441px;width:301px"></div>
  <svg class="icon" style="top:452px" width="12" height="12" viewBox="0 0 12 12"><path d="M2 1v11M2 1h8l-2 3 2 3H2" fill="none" stroke="#90949c" stroke-width="1.2"/></svg>
  <div class="abs info-row" style="top:451px">Created in 2016</div>
  <svg class="icon" style="top:480px" width="12" height="12" viewBox="0 0 12 12"><circle cx="6" cy="6" r="5" fill="none" stroke="#90949c" stroke-width="1.2"/><path d="M6 3v3l2 2" fill="none" stroke="#90949c" stroke-width="1.2"/></svg>
  <div class="abs info-row" style="top:479px">Mission</div>
  <div class="abs info-note" style="top:498px">To assist new &amp; existing businesses in creating and improving themselves whilst maximising their peoples potential.</div>

  <div class="abs section-head" style="left:274px;top:550px">CONTACT DETAILS</div>
  <div class="rule" style="left:274px;top:572px;width:301px"></div>
  <svg class="icon" style="top:585px" width="13" height="13" viewBox="0 0 13 13"><path d="M3 1l2 3-1.3 1.3c.8 1.7 2.2 3.1 3.9 3.9L9 7.9l3 2-1 2C6 12 1 7 1 2z" fill="none" stroke="#90949c" stroke-width="1.1"/></svg>
  <div class="abs info-row" style="top:584px">Call +44 20 7946 0321</div>
  <svg class="icon" style="top:613px" width="13" height="13" viewBox="0 0 13 13"><circle cx="6.5" cy="6.5" r="5.5" fill="none" stroke="#90949c" stroke-width="1.1"/></svg>
  <div class="abs info-row info-link" style="top:612px">m.me/Valdremoconsulting</div>
  <svg class="icon" style="top:643px" width="13" height="10" viewBox="0 0 13 10"><rect x=".5" y=".5" width="12" height="9" fill="none" stroke="#90949c"/><path d="M.5 .5l6 5 6-5" fill="none" stroke="#90949c"/></svg>
  <div class="abs info-row info-link" style="top:641px">martin.hale@valdremo.consulting</div>
  <svg class="icon" style="top:670px" width="13" height="13" viewBox="0 0 13 13"><circle cx="6.5" cy="6.5" r="5.5" fill="none" stroke="#90949c"/><ellipse cx="6.5" cy="6.5" rx="2.4" ry="5.5" fill="none" stroke="#90949c"/><line x1="1" y1="6.5" x2="12" y2="6.5" stroke="#90949c"/></svg>
  <div class="abs info-row info-link" style="top:669px">http://www.valdremo.consulting</div>

  <div class="abs section-head" style="left:274px;top:698px">MORE INFO</div>
  <div class="rule" style="left:274px;top:720px;width:301px"></div>
  <svg class="icon" style="top:732px" width="12" height="12" viewBox="0 0 12 12"><circle cx="6" cy="6" r="6" fill="#90949c"/><rect x="5.3" y="5" width="1.4" height="4.5" fill="#fff"/><circle cx="6" cy="3.3" r=".9" fill="#fff"/></svg>
  <div class="abs info-row" style="top:731px">About</div>
  <div class="abs info-note" style="top:750px;width:270px">VD Consulting we providing business development &amp; improvement services to small and medium enterprises and talented individuals.</div>
  <svg class="icon" style="top:802px" width="12" height="12" viewBox="0 0 12 12"><circle cx="6" cy="6" r="6" fill="#90949c"/><rect x="5.3" y="5" width="1.4" height="4.5" fill="#fff"/><circle cx="6" cy="3.3" r=".9" fill="#fff"/></svg>
  <div class="abs info-row" style="top:801px">Founding date</div>

  <div class="abs section-head" style="left:614px;top:418px">TEAM MEMBERS</div>
  <div class="rule" style="left:614px;top:441px;width:314px"></div>
  <div class="avatar" role="img" aria-label="Profile photo of team member"></div>
  <div class="abs member-name">Martin Hale</div>

</div>
</body>
</html>
```